Social Media Graphics - Harbor Climb REVISED

Create 6-7 individual social media graphics (square size) to encourage folks to join our online course called:

The Lantern Ledger Plan
How to Launch a Multi-Million Business From Scratch
Sign Up Today!

IMPORTANT: Make the largest and most prominent text on the graphic be: How to Launch a Multi-Million Business From Scratch

For the color scheme of the graphics, let's try a blue color palette; make sure the graphics appeal to both men and women

Make sure each graphic contains 1 of the 3 pics attached (crop pic as needed); and make sure one of the graphics is all TEXT only.

Target Market(s)

men and women looking to start a business

Industry/Entity Type

Entrepreneurship

Colors
0054AA
0677BA
7BADD7
CADEEF
E8F1F8

Requirements
Must have
• All the text and use the 3 pics provided; one graphic can be all text; Simple, modern design that's easy to read

```html
<!DOCTYPE html>
<html lang="en">
<head>
<meta charset="utf-8">
<title>The Lantern Ledger Plan – Sign Up</title>
<link href="https://fonts.googleapis.com/css2?family=Audiowide&display=swap" rel="stylesheet">
<style>
  :root {
    --blue-light: #4c95c9;
    --blue-mid: #2f77ae;
    --blue-deep: #1d5f94;
    --navy: #0c4470;
    --navy-dark: #0a3457;
    --ring: #3c86bd;
    --white: #ffffff;
  }
  html, body {
    margin: 0;
    padding: 0;
    width: 1200px;
    height: 1200px;
    overflow: hidden;
  }
  .poster {
    position: relative;
    width: 1200px;
    height: 1200px;
    overflow: hidden;
    background: radial-gradient(circle at 50% 50%, var(--blue-light) 0%, var(--blue-mid) 55%, var(--blue-deep) 100%);
    font-family: "Audiowide", sans-serif;
    color: var(--white);
  }
  .decor {
    position: absolute;
    inset: 0;
  }
  .headline {
    position: absolute;
    left: 0;
    width: 1200px;
    margin: 0;
    text-align: center;
    line-height: 1;
    font-weight: 400;
    text-shadow: 0 3px 6px rgba(0, 0, 0, 0.35);
  }
  .headline--top { top: 18px; font-size: 104px; }
  .headline--bottom { top: 220px; font-size: 112px; }
  .headline-box {
    position: absolute;
    top: 120px;
    left: 30px;
    width: 1134px;
    height: 88px;
    border: 3px solid var(--white);
    background: var(--navy-dark);
    display: flex;
    align-items: center;
    justify-content: center;
    font-size: 72px;
    line-height: 1;
    margin: 0;
    font-weight: 400;
  }
  .program-name {
    position: absolute;
    top: 860px;
    left: 0;
    width: 1200px;
    margin: 0;
    text-align: center;
    font-size: 110px;
    line-height: 1.12;
    font-weight: 400;
    letter-spacing: -2px;
    text-shadow: 0 4px 8px rgba(0, 0, 0, 0.4);
  }
  .cta-band {
    position: absolute;
    left: 0;
    bottom: 0;
    width: 1200px;
    height: 80px;
    background: var(--navy-dark);
    display: flex;
    align-items: center;
    justify-content: center;
    font-size: 44px;
  }
</style>
</head>
<body>
<main class="poster">
  <svg class="decor" width="1200" height="1200" viewBox="0 0 1200 1200">
    <defs>
      <radialGradient id="photoTone" cx="50%" cy="45%" r="60%">
        <stop offset="0%" stop-color="#2a5f8c"/>
        <stop offset="100%" stop-color="#0e3d66"/>
      </radialGradient>
    </defs>
    <circle class="side-ring" cx="70" cy="610" r="200" fill="none" stroke="var(--navy)" stroke-width="95"/>
    <circle class="side-ring" cx="1130" cy="610" r="200" fill="none" stroke="var(--navy)" stroke-width="95"/>
    <circle class="photo-frame" cx="600" cy="625" r="340" fill="var(--ring)"/>
    <circle class="photo-frame" cx="600" cy="625" r="322" fill="var(--navy)"/>
    <circle class="photo" cx="600" cy="640" r="300" fill="url(#photoTone)" role="img" aria-label="Photo of the two course hosts smiling, one in a black turtleneck with arms crossed, one in a denim jacket"/>
  </svg>

  <h1 class="headline headline--top">HOW TO LAUNCH A</h1>
  <h2 class="headline-box">MULTI-MILLION BUSINESS</h2>
  <h1 class="headline headline--bottom">FROM SCRATCH</h1>

  <p class="program-name">IT’S LANTERN<br>LEDGER PLAN</p>

  <div class="cta-band">SIGN UP TODAY!</div>
</main>
</body>
</html>
```